One Thumbnail for Online Shop for PowerPoint Templates needed

We are selling PowerPoint Templates and need therefore a thumbnail for our online shop.

You can use a stock photo, mock-ups or other design elements.

Format:
squared like 500 x 500
or wide like 1280 x 720

If you want to use a title, use:

"Graphs" ---> Title
"PowerPoint template" ---> subtitle

Attachments:
- OLD: Our old thumbnail which I do not like
- Template: PowerPoint pictures which you can use ( you can also copy them if you need more than these)
- Example: Some examples I found from other shops (please do not copy them exactly, only to show what I mean)

I received lots of designs until now but many are not what I have expected

Target Market(s)

E-Commerce

Industry/Entity Type

Shop

Font styles to use
Sans Serif

Requirements
Should not have
• Do NOT re-design one of the template.png (these are only examples, I will replace them later)

```html
<!DOCTYPE html>
<html lang="en">
<head>
<meta charset="utf-8">
<title>Standard Graphs – Slide Show Template</title>
<link rel="stylesheet" href="https://fonts.googleapis.com/css2?family=Michroma&family=Lato:wght@300;400;700&display=swap">
<style>
  :root {
    --bg-deep: #141a45;
    --bg-mid: #2a2f66;
    --bg-haze: #4a4c85;
    --slide-bg: #f5f7fa;
    --bar-dark: #1f3b73;
    --bar-light: #4a8fd6;
    --ink: #1c1c1c;
    --ink-soft: #555a63;
    --grid: #d6dbe3;
    --title-white: #ffffff;
  }
  html, body { margin: 0; padding: 0; overflow: hidden; }
  body { width: 1200px; height: 754px; position: relative; background: var(--bg-deep); font-family: "Lato", sans-serif; }
  .backdrop {
    position: absolute; inset: 0;
    background:
      radial-gradient(ellipse 420px 300px at 690px 230px, rgba(150,160,210,.45), transparent 70%),
      radial-gradient(ellipse 500px 260px at 980px 150px, rgba(110,110,170,.35), transparent 70%),
      linear-gradient(180deg, var(--bg-haze) 0%, var(--bg-mid) 45%, var(--bg-deep) 100%);
  }
  .slide {
    position: absolute; width: 324px; height: 182px;
    background: var(--slide-bg);
    box-shadow: 0 4px 14px rgba(0,0,0,.45);
  }
  .slide svg { display: block; width: 100%; height: 100%; }
  .slide--grid { left: 74px; top: 69px; }
  .slide--combo { left: 74px; top: 287px; }
  .slide--ranking { left: 72px; top: 506px; }
  .s-title { font: 700 12px "Lato", sans-serif; fill: var(--ink); }
  .s-sub { font: 400 6.6px "Lato", sans-serif; fill: var(--ink); }
  .s-label { font: 700 5px "Lato", sans-serif; fill: var(--ink); }
  .s-tiny { font: 400 3.3px "Lato", sans-serif; fill: var(--ink-soft); }
  .s-body { font: 400 4.8px "Lato", sans-serif; fill: var(--ink-soft); }
  .s-val { font: 400 5.5px "Lato", sans-serif; fill: #8a8f98; }
  .s-in { font: 400 5.5px "Lato", sans-serif; fill: #fff; }
  .s-acc { font: 400 5px "Lato", sans-serif; fill: var(--bar-light); }
  .dark { fill: var(--bar-dark); }
  .light { fill: var(--bar-light); }
  .headline {
    position: absolute; right: 87px; top: 454px; margin: 0;
    font-family: "Michroma", sans-serif; font-weight: 400; color: var(--title-white);
    font-size: 90px; line-height: 76px; text-align: right; letter-spacing: -1px; white-space: nowrap;
  }
  .subline {
    position: absolute; right: 84px; top: 633px; margin: 0;
    font-family: "Lato", sans-serif; font-weight: 300; color: var(--title-white);
    font-size: 58px; line-height: 64px; white-space: nowrap;
  }
</style>
</head>
<body>
  <div class="backdrop" role="img" aria-label="Dimmed photo of a desk with a desktop monitor showing chart slides, tinted deep blue"></div>

  <div class="slide slide--grid">
    <svg viewBox="0 0 405 228">
      <defs>
        <g id="mini-a">
          <g stroke="var(--grid)" stroke-width=".5"><line x1="0" y1="0" x2="112" y2="0"/><line x1="0" y1="14" x2="112" y2="14"/><line x1="0" y1="28" x2="112" y2="28"/><line x1="0" y1="42" x2="112" y2="42"/><line x1="0" y1="56" x2="112" y2="56"/></g>
          <g class="light"><rect x="6" y="34" width="5" height="22"/><rect x="16" y="26" width="5" height="30"/><rect x="26" y="11" width="5" height="45"/><rect x="36" y="21" width="5" height="35"/><rect x="46" y="18" width="5" height="38"/><rect x="56" y="26" width="5" height="30"/><rect x="66" y="31" width="5" height="25"/><rect x="76" y="34" width="5" height="22"/><rect x="86" y="28" width="5" height="28"/><rect x="96" y="36" width="5" height="20"/><rect x="106" y="26" width="5" height="30"/></g>
          <g class="dark"><rect x="6" y="42" width="5" height="14"/><rect x="16" y="36" width="5" height="20"/><rect x="26" y="34" width="5" height="22"/><rect x="36" y="36" width="5" height="20"/><rect x="46" y="36" width="5" height="20"/><rect x="56" y="37" width="5" height="19"/><rect x="66" y="38" width="5" height="18"/><rect x="76" y="41" width="5" height="15"/><rect x="86" y="39" width="5" height="17"/><rect x="96" y="38" width="5" height="18"/><rect x="106" y="39" width="5" height="17"/></g>
          <text class="s-tiny" y="61">Text Text Text Text Text Text Text Text Text Text Text</text>
        </g>
        <g id="mini-b">
          <g stroke="var(--grid)" stroke-width=".5"><line x1="0" y1="0" x2="112" y2="0"/><line x1="0" y1="14" x2="112" y2="14"/><line x1="0" y1="28" x2="112" y2="28"/><line x1="0" y1="42" x2="112" y2="42"/><line x1="0" y1="56" x2="112" y2="56"/></g>
          <g class="light"><rect x="6" y="24" width="5" height="32"/><rect x="16" y="30" width="5" height="26"/><rect x="26" y="20" width="5" height="36"/><rect x="36" y="6" width="5" height="50"/><rect x="46" y="12" width="5" height="44"/><rect x="56" y="26" width="5" height="30"/><rect x="66" y="30" width="5" height="26"/><rect x="76" y="16" width="5" height="40"/><rect x="86" y="34" width="5" height="22"/><rect x="96" y="22" width="5" height="34"/><rect x="106" y="30" width="5" height="26"/></g>
          <g class="dark"><rect x="6" y="40" width="5" height="16"/><rect x="16" y="42" width="5" height="14"/><rect x="26" y="38" width="5" height="18"/><rect x="36" y="32" width="5" height="24"/><rect x="46" y="36" width="5" height="20"/><rect x="56" y="38" width="5" height="18"/><rect x="66" y="41" width="5" height="15"/><rect x="76" y="30" width="5" height="26"/><rect x="86" y="42" width="5" height="14"/><rect x="96" y="34" width="5" height="22"/><rect x="106" y="40" width="5" height="16"/></g>
          <text class="s-tiny" y="61">Text Text Text Text Text Text Text Text Text Text Text</text>
        </g>
      </defs>
      <text class="s-title" x="202" y="20" text-anchor="middle">Lorem ipsum dolor sit amet</text>
      <text class="s-sub" x="202" y="35" text-anchor="middle">Lorem ipsum dolor sit amet, consectetuer adipiscing elit. Aenean commodo ligula eget dolor.</text>

      <text class="s-label" x="28" y="58">Lorem ipsum</text><text class="s-tiny" x="28" y="63">Lorem ipsum dolor sit amet, consetetur sadipscing elitr</text>
      <use href="#mini-a" x="30" y="68"/>
      <text class="s-label" x="158" y="58">Lorem ipsum</text><text class="s-tiny" x="158" y="63">Lorem ipsum dolor sit amet, consetetur sadipscing elitr</text>
      <use href="#mini-b" x="160" y="68"/>
      <text class="s-label" x="28" y="142">Lorem ipsum</text><text class="s-tiny" x="28" y="147">Lorem ipsum dolor sit amet, consetetur sadipscing elitr</text>
      <use href="#mini-b" x="30" y="150"/>
      <text class="s-label" x="158" y="142">Lorem ipsum</text><text class="s-tiny" x="158" y="147">Lorem ipsum dolor sit amet, consetetur sadipscing elitr</text>
      <use href="#mini-a" x="160" y="150"/>

      <g class="s-tiny">
        <text x="305" y="78">Lorem ipsum dolor sit amet, consetetur</text><text x="305" y="84">sadipscing elitr, sed diam nonumy</text><text x="305" y="90">eirmod tempor invidunt ut labore et</text><text x="305" y="96">dolore magna aliquyam erat, sed diam</text><text x="305" y="102">voluptua. At vero eos et accusam</text>
        <text x="305" y="124">Lorem ipsum dolor sit amet, consetetur</text><text x="305" y="130">sadipscing elitr, sed diam nonumy</text><text x="305" y="136">eirmod tempor invidunt ut labore et</text><text x="305" y="142">dolore magna aliquyam erat, sed diam</text><text x="305" y="148">voluptua. At vero eos et accusam</text>
        <text x="305" y="170">Lorem ipsum dolor sit amet, consetetur</text><text x="305" y="176">sadipscing elitr, sed diam nonumy</text><text x="305" y="182">eirmod tempor invidunt ut labore et</text><text x="305" y="188">dolore magna aliquyam erat, sed diam</text><text x="305" y="194">voluptua. At vero eos et accusam</text>
      </g>
    </svg>
  </div>

  <div class="slide slide--combo">
    <svg viewBox="0 0 405 228">
      <text class="s-title" x="202" y="20" text-anchor="middle">Lorem ipsum dolor sit amet</text>
      <text class="s-sub" x="202" y="35" text-anchor="middle">Lorem ipsum dolor sit amet, consectetuer adipiscing elit. Aenean commodo ligula eget dolor.</text>
      <g class="s-body">
        <text x="32" y="96">Lorem ipsum dolor sit amet,</text><text x="32" y="103">consetetur sadipscing elitr,</text><text x="32" y="110">sed diam nonumy eirmod</text><text x="32" y="117">tempor invidunt ut labore et</text><text x="32" y="124">dolore magna aliquyam erat,</text><text x="32" y="131">sed diam voluptua. At vero</text><text x="32" y="138">eos et accusam</text>
        <text x="32" y="156">Lorem ipsum dolor sit amet,</text><text x="32" y="163">consetetur sadipscing elitr,</text><text x="32" y="170">sed diam nonumy eirmod</text><text x="32" y="177">tempor invidunt ut labore et</text><text x="32" y="184">dolore magna aliquyam erat,</text><text x="32" y="191">sed diam voluptua. At vero</text><text x="32" y="198">eos et accusam</text>
      </g>
      <circle cx="23" cy="94" r="1" fill="#8a8f98"/><circle cx="23" cy="154" r="1" fill="#8a8f98"/>
      <g class="light">
        <rect x="123" y="158" width="11" height="42"/><rect x="141.5" y="155" width="11" height="45"/><rect x="160" y="145" width="11" height="55"/><rect x="178.5" y="132" width="11" height="68"/><rect x="197" y="129" width="11" height="71"/><rect x="215.5" y="122" width="11" height="78"/><rect x="234" y="116" width="11" height="84"/><rect x="252.5" y="106" width="11" height="94"/><rect x="271" y="106" width="11" height="94"/><rect x="289.5" y="99" width="11" height="101"/><rect x="308" y="96" width="11" height="104"/><rect x="326.5" y="90" width="11" height="110"/>
      </g>
      <g class="s-in" text-anchor="middle">
        <text x="128.5" y="182">13</text><text x="147" y="180">14</text><text x="165.5" y="175">17</text><text x="184" y="168">21</text><text x="202.5" y="167">22</text><text x="221" y="163">24</text><text x="239.5" y="160">26</text><text x="258" y="156">29</text><text x="276.5" y="156">29</text><text x="295" y="152">31</text><text x="313.5" y="151">32</text><text x="332" y="148">34</text>
      </g>
      <polyline fill="none" stroke="#9aa0a8" stroke-width=".8" points="128.5,148 147,144 165.5,134 184,122 202.5,118 221,107 239.5,96 258,88 276.5,88 295,81 313.5,75 332,75"/>
      <g fill="#fff" stroke="#9aa0a8" stroke-width=".7">
        <circle cx="128.5" cy="148" r="1.6"/><circle cx="147" cy="144" r="1.6"/><circle cx="165.5" cy="134" r="1.6"/><circle cx="184" cy="122" r="1.6"/><circle cx="202.5" cy="118" r="1.6"/><circle cx="221" cy="107" r="1.6"/><circle cx="239.5" cy="96" r="1.6"/><circle cx="258" cy="88" r="1.6"/><circle cx="276.5" cy="88" r="1.6"/><circle cx="295" cy="81" r="1.6"/><circle cx="313.5" cy="75" r="1.6"/><circle cx="332" cy="75" r="1.6"/>
      </g>
      <g class="s-val" text-anchor="middle">
        <text x="128.5" y="142">16</text><text x="147" y="138">17</text><text x="165.5" y="128">20</text><text x="184" y="116">24</text><text x="202.5" y="112">25</text><text x="221" y="101">27</text><text x="239.5" y="90">29</text><text x="258" y="82">32</text><text x="276.5" y="82">32</text><text x="295" y="75">34</text><text x="313.5" y="69">36</text><text x="332" y="69">36</text>
        <text x="128.5" y="210">Text</text><text x="147" y="210">Text</text><text x="165.5" y="210">Text</text><text x="184" y="210">Text</text><text x="202.5" y="210">Text</text><text x="221" y="210">Text</text><text x="239.5" y="210">Text</text><text x="258" y="210">Text</text><text x="276.5" y="210">Text</text><text x="295" y="210">Text</text><text x="313.5" y="210">Text</text><text x="332" y="210">Text</text>
      </g>
      <text class="s-val" x="341" y="84">Lorem ipsum</text>
      <text class="s-acc" x="341" y="147">Lorem ipsum</text>
    </svg>
  </div>

  <div class="slide slide--ranking">
    <svg viewBox="0 0 405 228">
      <text class="s-title" x="202" y="20" text-anchor="middle">Lorem ipsum dolor sit amet</text>
      <text class="s-sub" x="202" y="35" text-anchor="middle">Lorem ipsum dolor sit amet, consectetuer adipiscing elit. Aenean commodo ligula eget dolor.</text>
      <text class="s-label" x="41" y="54">Lorem ipsum</text>
      <text class="s-tiny" x="41" y="60" style="font-size:4.4px">Lorem ipsum dolor sit amet, consetetur sadipscing elitr, sed diam nonumy eirmod tempor</text>
      <text class="s-tiny" x="41" y="66" style="font-size:4.4px">invidunt ut labore et dolore magna aliquyam erat, sed diam voluptua. At vero eos et accusam</text>
      <g stroke="var(--grid)" stroke-width=".6">
        <line x1="40" y1="87" x2="190" y2="87"/><line x1="40" y1="99" x2="190" y2="99"/><line x1="40" y1="112" x2="190" y2="112"/><line x1="40" y1="124" x2="190" y2="124"/><line x1="40" y1="136" x2="190" y2="136"/><line x1="40" y1="149" x2="190" y2="149"/><line x1="40" y1="161" x2="190" y2="161"/><line x1="40" y1="173" x2="190" y2="173"/><line x1="40" y1="186" x2="190" y2="186"/>
        <line x1="200" y1="87" x2="290" y2="87"/><line x1="200" y1="99" x2="290" y2="99"/><line x1="200" y1="112" x2="290" y2="112"/><line x1="200" y1="124" x2="290" y2="124"/><line x1="200" y1="136" x2="290" y2="136"/><line x1="200" y1="149" x2="290" y2="149"/><line x1="200" y1="161" x2="290" y2="161"/><line x1="200" y1="173" x2="290" y2="173"/><line x1="200" y1="186" x2="290" y2="186"/>
      </g>
      <g class="dark">
        <rect x="42" y="78" width="113" height="5.5"/><rect x="42" y="90" width="106" height="5.5"/><rect x="42" y="103" width="106" height="5.5"/><rect x="42" y="115" width="95" height="5.5"/><rect x="42" y="127" width="88" height="5.5"/><rect x="42" y="140" width="80" height="5.5"/><rect x="42" y="152" width="77" height="5.5"/><rect x="42" y="164" width="62" height="5.5"/><rect x="42" y="177" width="51" height="5.5"/><rect x="42" y="189" width="47" height="5.5"/>
      </g>
      <g class="s-tiny" style="font-size:5px;fill:var(--ink)">
        <text x="27" y="83">Text</text><text x="27" y="95">Text</text><text x="27" y="108">Text</text><text x="27" y="120">Text</text><text x="27" y="132">Text</text><text x="27" y="145">Text</text><text x="27" y="157">Text</text><text x="27" y="169">Text</text><text x="27" y="182">Text</text><text x="27" y="194">Text</text>
        <text x="158" y="83">31</text><text x="151" y="95">29</text><text x="151" y="108">29</text><text x="140" y="120">26</text><text x="133" y="132">24</text><text x="125" y="145">22</text><text x="122" y="157">21</text><text x="107" y="169">17</text><text x="96" y="182">14</text><text x="92" y="194">13</text>
      </g>
      <g class="light">
        <rect x="235" y="78" width="25" height="5.5"/><rect x="235" y="90" width="34" height="5.5"/><rect x="218" y="103" width="17" height="5.5"/><rect x="227" y="115" width="8" height="5.5"/><rect x="235" y="127" width="25" height="5.5"/><rect x="235" y="140" width="25" height="5.5"/><rect x="235" y="152" width="8" height="5.5"/><rect x="227" y="164" width="8" height="5.5"/><rect x="235" y="177" width="34" height="5.5"/><rect x="235" y="189" width="17" height="5.5"/>
      </g>
      <g class="s-acc" style="font-size:4.4px">
        <text x="263" y="83">+3%</text><text x="272" y="95">+4%</text><text x="204" y="108">-2%</text><text x="213" y="120">-1%</text><text x="263" y="132">+3%</text><text x="263" y="145">+3%</text><text x="246" y="157">+1%</text><text x="213" y="169">-1%</text><text x="272" y="182">+4%</text><text x="255" y="194">+2%</text>
      </g>
      <g class="s-tiny">
        <text x="300" y="80">Lorem ipsum dolor sit amet,</text><text x="300" y="86">consetetur sadipscing elitr, sed</text><text x="300" y="92">diam nonumy eirmod tempor</text><text x="300" y="98">invidunt ut labore et dolore magna</text><text x="300" y="104">aliquyam erat, sed diam voluptua.</text><text x="300" y="110">At vero eos et accusam</text>
        <text x="300" y="126">Lorem ipsum dolor sit amet,</text><text x="300" y="132">consetetur sadipscing elitr, sed</text><text x="300" y="138">diam nonumy eirmod tempor</text><text x="300" y="144">invidunt ut labore et dolore magna</text><text x="300" y="150">aliquyam erat, sed diam voluptua.</text><text x="300" y="156">At vero eos et accusam</text>
        <text x="300" y="172">Lorem ipsum dolor sit amet,</text><text x="300" y="178">consetetur sadipscing elitr, sed</text><text x="300" y="184">diam nonumy eirmod tempor</text><text x="300" y="190">invidunt ut labore et dolore magna</text><text x="300" y="196">aliquyam erat, sed diam voluptua.</text><text x="300" y="202">At vero eos et accusam</text>
      </g>
    </svg>
  </div>

  <h1 class="headline">Standard<br>Graphs</h1>
  <p class="subline">Slide Show Presentation 1</p>
</body>
</html>
```